Security Warning Sign

We have an existing sign that needs an update. I have attached a picture of the current square sign. We need to maintain the same wording. It needs to be professional and appropriate to attach to our customers fence. Also attached is a copy of our building sign which may lend some inspiration and hopefully the ai format will assist. The final sign will be 600mm x 600mmOur website is www.harbourlinewatch.com.au

```html
<!DOCTYPE html>
<html lang="en">
<head>
<meta charset="utf-8">
<title>Security Warning Sign</title>
<link rel="stylesheet" href="https://fonts.googleapis.com/css2?family=Oswald:wght@700&family=Open+Sans:wght@700;800&display=swap">
<style>
  :root {
    --orange: #ef8228;
    --ink: #1d1a1c;
    --white: #ffffff;
    --stripe-grey: #9a9a9a;
    --page: #2a2a2a;
    --facet-light: #f6f6f6;
    --facet-mid: #e8e8e8;
    --camera-tone: #dcdcdc;
  }
  * { margin: 0; padding: 0; box-sizing: border-box; }
  html, body { width: 1200px; height: 900px; overflow: hidden; }
  body { background: var(--page); position: relative; }

  .sign {
    position: absolute; left: 243px; top: 93px;
    width: 714px; height: 714px;
    background: linear-gradient(135deg, var(--white) 0%, var(--facet-light) 40%, var(--facet-mid) 65%, var(--facet-light) 85%, var(--white) 100%);
    overflow: hidden;
    font-family: "Open Sans", Arial, sans-serif;
  }
  .sign__camera {
    position: absolute; left: 557px; top: 142px;
    width: 157px; height: 212px;
    z-index: 0;
  }
  .sign__headline {
    position: absolute; left: 85px; top: 52px;
    width: 556px; height: 136px;
    z-index: 1;
  }
  .sign__headline text {
    font-family: "Oswald", "Arial Narrow", sans-serif;
    font-weight: 700; font-size: 162px;
    fill: var(--orange);
  }
  .sign__message {
    position: absolute; left: 124px; top: 212px;
    font-weight: 800; font-size: 63px; line-height: 90px;
    letter-spacing: -1px;
    color: var(--ink);
    z-index: 1;
  }
  .brand {
    position: absolute; left: 30px; top: 583px;
    display: flex; align-items: center; gap: 14px;
  }
  .brand__dot { width: 70px; height: 70px; border-radius: 50%; background: var(--orange); flex: none; }
  .brand__name {
    font-weight: 800; font-size: 17px; line-height: 21px;
    text-transform: uppercase; color: var(--ink); letter-spacing: 0.5px;
  }
  .contact-band {
    position: absolute; left: 308px; top: 590px;
    width: 406px; height: 62px;
  }
  .contact-band__stripes { position: absolute; left: 0; top: 0; width: 100%; height: 100%; }
  .contact-band__phone {
    position: absolute; left: 50px; top: 0; height: 62px;
    display: flex; align-items: center; gap: 12px;
    font-weight: 800; font-size: 38px; color: var(--white);
    white-space: nowrap;
  }
  .contact-band__icon { width: 38px; height: 38px; flex: none; }
  .sign__footer {
    position: absolute; left: 0; bottom: 0;
    width: 100%; height: 42px;
    background: var(--ink);
    display: flex; align-items: center; justify-content: center;
    font-weight: 700; font-size: 18px; color: var(--white);
    text-transform: uppercase; letter-spacing: 0.5px;
  }
</style>
</head>
<body>
  <main class="sign">
    <svg class="sign__camera" role="img" aria-label="Illustration of a security camera" viewBox="0 0 157 212">
      <rect x="0" y="0" width="157" height="212" fill="var(--camera-tone)" opacity="0.5"/>
    </svg>

    <svg class="sign__headline" viewBox="0 0 556 136">
      <text x="0" y="132" textLength="556" lengthAdjust="spacingAndGlyphs">WARNING</text>
    </svg>

    <p class="sign__message">Electronic<br>surveillance<br>devices installed<br>in this area.</p>

    <div class="brand">
      <span class="brand__dot"></span>
      <span class="brand__name">Harbourline<br>Watch<br>Services</span>
    </div>

    <div class="contact-band">
      <svg class="contact-band__stripes" viewBox="0 0 406 62" preserveAspectRatio="none" aria-hidden="true">
        <polygon points="0,62 38,0 46,0 8,62" fill="var(--stripe-grey)"/>
        <polygon points="18,62 56,0 67,0 29,62" fill="var(--orange)"/>
        <polygon points="38,62 76,0 406,0 406,62" fill="var(--orange)"/>
      </svg>
      <div class="contact-band__phone">
        <svg class="contact-band__icon" viewBox="0 0 24 24" aria-hidden="true">
          <path fill="var(--ink)" d="M6.6 10.8a15.1 15.1 0 0 0 6.6 6.6l2.2-2.2a1 1 0 0 1 1-.25 11.4 11.4 0 0 0 3.6.57 1 1 0 0 1 1 1V20a1 1 0 0 1-1 1A17 17 0 0 1 3 4a1 1 0 0 1 1-1h3.5a1 1 0 0 1 1 1c0 1.25.2 2.45.57 3.57a1 1 0 0 1-.25 1z"/>
        </svg>
        <span>1300 555 014</span>
      </div>
    </div>

    <footer class="sign__footer">harbourlinewatch.com.au</footer>
  </main>
</body>
</html>
```